Career Management Consultant Fun Professional Business Card

This is a business card for a personal career management consultant. The vibe needs to be professional but fun, modern with colour.

The name of the business is "Marcus Telwanger Career Management Consulting"

The name of the individual is "Marcus Telwanger" and his title is "Career Management Consultant"

Industry/Entity Type

Business

Contact Information for Business Card

Marcus Telwanger
Phone: 0400 827 316
Email: Marcus.Telwanger@mailvessa.com

```html
<!DOCTYPE html>
<html lang="en">
<head>
<meta charset="utf-8">
<title>Marcus Telwanger — Business Card</title>
<link href="https://fonts.googleapis.com/css2?family=Josefin+Sans:wght@300;400;600&display=swap" rel="stylesheet">
<style>
  :root {
    --ink: #111111;
    --paper: #ffffff;
    --stage: #e9e6e2;
    --accent: #14a39a;
    --accent-warm: #f2a33a;
    --mark-faint: #f1f1f1;
    --muted: #2b2b2b;
  }
  * { box-sizing: border-box; margin: 0; padding: 0; }
  html, body { width: 1200px; height: 945px; overflow: hidden; }
  body {
    background: var(--stage);
    font-family: "Josefin Sans", "Helvetica Neue", Arial, sans-serif;
    color: var(--ink);
    display: flex;
    align-items: center;
    justify-content: center;
    gap: 60px;
  }
  .card {
    width: 540px;
    height: 310px;
    background: var(--paper);
    position: relative;
    overflow: hidden;
    box-shadow: 0 6px 18px rgba(0,0,0,0.12);
  }

  /* Front */
  .card--front {
    display: flex;
    align-items: center;
    justify-content: center;
  }
  .lockup { display: flex; align-items: center; gap: 18px; }
  .lockup__square { width: 58px; height: 58px; background: var(--accent); flex: none; }
  .lockup__name {
    font-weight: 400;
    font-size: 30px;
    letter-spacing: 2px;
    text-transform: uppercase;
    line-height: 1;
  }
  .lockup__tagline {
    margin-top: 8px;
    font-weight: 400;
    font-size: 11px;
    letter-spacing: 1.6px;
    text-transform: uppercase;
    color: var(--muted);
  }

  /* Back */
  .watermark {
    position: absolute;
    left: -40px;
    top: 70px;
    width: 260px;
    height: 260px;
    background: var(--mark-faint);
  }
  .brand-mini {
    position: absolute;
    top: 34px;
    right: 36px;
    display: flex;
    align-items: center;
    gap: 10px;
  }
  .brand-mini__square { width: 26px; height: 26px; background: var(--accent); flex: none; }
  .brand-mini__text {
    font-size: 9px;
    font-weight: 400;
    letter-spacing: 1.2px;
    text-transform: uppercase;
    line-height: 1.5;
  }
  .holder {
    position: absolute;
    top: 118px;
    left: 150px;
    right: 36px;
  }
  .holder__name {
    font-size: 21px;
    font-weight: 400;
    letter-spacing: 1.5px;
    text-transform: uppercase;
    padding: 0 0 8px 8px;
  }
  .holder__rule { height: 2px; background: var(--accent-warm); }
  .contacts {
    position: absolute;
    left: 36px;
    bottom: 34px;
    list-style: none;
    display: flex;
    flex-direction: column;
    gap: 9px;
  }
  .contacts__item {
    display: flex;
    align-items: center;
    gap: 8px;
    font-size: 12px;
    font-weight: 400;
    letter-spacing: 0.8px;
    color: var(--muted);
  }
  .contacts__item--email { text-transform: uppercase; }
  .contacts__icon { width: 15px; height: 15px; flex: none; }
</style>
</head>
<body>
  <section class="card card--front" aria-label="Card front">
    <div class="lockup">
      <span class="lockup__square" aria-hidden="true"></span>
      <div>
        <p class="lockup__name">Marcus Telwanger</p>
        <p class="lockup__tagline">Career Management Consulting</p>
      </div>
    </div>
  </section>

  <section class="card card--back" aria-label="Card back">
    <span class="watermark" aria-hidden="true"></span>

    <div class="brand-mini">
      <span class="brand-mini__square" aria-hidden="true"></span>
      <p class="brand-mini__text">Marcus Telwanger<br>Career Management Consulting</p>
    </div>

    <div class="holder">
      <p class="holder__name">Marcus Telwanger</p>
      <div class="holder__rule"></div>
    </div>

    <ul class="contacts">
      <li class="contacts__item">
        <svg class="contacts__icon" viewBox="0 0 16 16" aria-hidden="true">
          <rect width="16" height="16" rx="3" fill="#14a39a"/>
          <path d="M5.2 3.6l1.6 1.9-.9 1.1c.6 1.3 1.5 2.2 2.7 2.8l1-.9 2 1.5-.8 1.7c-3.6-.3-6.7-3.4-7-7z" fill="#fff"/>
        </svg>
        <span>0400 827 316</span>
      </li>
      <li class="contacts__item contacts__item--email">
        <svg class="contacts__icon" viewBox="0 0 16 16" aria-hidden="true">
          <rect width="16" height="16" rx="3" fill="#14a39a"/>
          <circle cx="8" cy="8" r="2" fill="none" stroke="#fff" stroke-width="1.2"/>
          <path d="M10 6.2v2.6c0 1 1.6 1 1.6-.6A3.6 3.6 0 1 0 9.8 11" fill="none" stroke="#fff" stroke-width="1.2" stroke-linecap="round"/>
        </svg>
        <span>Marcus.Telwanger@mailvessa.com</span>
      </li>
    </ul>
  </section>
</body>
</html>
```